Commercial Cleaning Company Needs A Flyer

We are a commercial cleaning company based in London.
We are currently trying to grow our client base and would like a fresh, professional flyer that differentiates us from the competition. We mainly specialises in commercial cleaning such as offices, educational facilities etc. I would like to see a flyer design that look professional, unique not cheap. I have attached a file that contains some company details but Im happy to explore other options if thay are relevant. Please also find company Claremont and colour chart, this should remain as is.

I have attached some pictures that contain diamond shaped windows. I feel that this can be used to represent and incorporate the Claremont. Please add to flyer where possible.

Please feel free to contact me for any further advice.
Thanks and good luck

Target Market(s)

commercial buildings and residential property owners

Industry/Entity Type

Cleaning Service

Contact Information for Business Card

Please refer to up loaded document for company details and Claremont colours.

Font styles to use
Sans Serif

Colors
33a6d7
33b8a4

Requirements
Must have
• Look Professional, not cheap, unique, stand out from others.

```html
<!DOCTYPE html>
<html lang="en">
<head>
<meta charset="utf-8">
<title>Cleaning Company Flyer</title>
<link href="https://fonts.googleapis.com/css2?family=Russo+One&family=Mulish:wght@400;600;700;800&display=swap" rel="stylesheet">
<style>
  :root {
    --purple: #372b8e;
    --teal: #33b8a4;
    --teal-light: #4cc7b5;
    --teal-deep: #2aa892;
    --white: #ffffff;
    --ink: #2b2b3a;
    --stage: #e6e6ec;
    --photo-a: #c9d3dc;
    --photo-b: #8fa6b8;
  }
  * { box-sizing: border-box; margin: 0; padding: 0; }
  html, body { width: 1041px; height: 1200px; overflow: hidden; }
  body { background: var(--stage); font-family: "Mulish", sans-serif; position: relative; }

  .flyer {
    position: absolute; left: 112px; top: 24px;
    width: 816px; height: 1153px;
    background: var(--white); overflow: hidden;
    box-shadow: 0 10px 30px rgba(0,0,0,.18);
  }
  .flyer-shapes { position: absolute; inset: 0; }

  .brand {
    position: absolute; right: 44px; top: 48px;
    font-family: "Mulish", sans-serif; font-weight: 800;
    font-size: 40px; color: var(--purple); letter-spacing: -0.5px;
  }

  .inset-photo {
    position: absolute; left: 39px; top: 375px;
    width: 156px; height: 156px; border-radius: 50%;
    border: 5px solid var(--white);
    background: radial-gradient(circle at 40% 40%, #eef0f2, #aab6c0);
    box-shadow: 0 4px 10px rgba(0,0,0,.2);
  }

  .headline {
    position: absolute; left: 0; right: 0; top: 522px; text-align: center;
    font-family: "Russo One", sans-serif; font-size: 30px;
    color: var(--purple); letter-spacing: 0.5px;
  }
  .intro {
    position: absolute; left: 0; right: 0; top: 572px; text-align: center;
    font-size: 23px; color: var(--ink); letter-spacing: 0.3px;
  }
  .intro mark {
    background: var(--purple); color: var(--white);
    padding: 0 4px; border-radius: 4px;
  }

  .sectors { position: absolute; left: 0; top: 638px; width: 816px; height: 130px; }
  .sector {
    position: absolute; top: 0; width: 170px; margin-left: -85px;
    text-align: center; color: var(--white);
  }
  .sector svg { display: block; margin: 0 auto; }
  .sector-name { display: block; margin-top: 12px; font-size: 16px; }
  .sector-divider {
    position: absolute; top: 2px; width: 2px; height: 96px; background: var(--purple);
  }

  .benefits-tab {
    position: absolute; left: 0; top: 868px; width: 368px; height: 45px;
    background: var(--purple); border-radius: 0 14px 14px 0;
    color: var(--white); font-family: "Russo One", sans-serif;
    font-size: 24px; line-height: 45px; padding-left: 26px; letter-spacing: 0.5px;
  }
  .benefits-col { position: absolute; top: 941px; list-style: none; }
  .benefits-col li {
    position: relative; padding-left: 26px; height: 28px;
    font-size: 13px; color: var(--ink); line-height: 20px;
  }
  .benefits-col li.tall { height: 40px; line-height: 16px; padding-top: 2px; }
  .benefits-col li svg { position: absolute; left: 0; top: 3px; }

  .call-now {
    position: absolute; left: 485px; top: 1043px; width: 331px; height: 68px;
    background: var(--purple); border-radius: 34px 0 0 34px;
    color: var(--white); font-family: "Russo One", sans-serif; font-size: 23px;
    display: flex; align-items: center; padding-left: 22px; gap: 12px;
  }
  .call-now .sep { width: 2px; height: 40px; background: var(--white); }

  .footer {
    position: absolute; left: 0; right: 0; bottom: 0; height: 49px;
    background: var(--teal); border-top: 4px solid var(--purple);
    color: var(--white);
  }
  .footer-address {
    position: absolute; left: 43px; top: 13px; font-size: 14px;
    display: flex; align-items: center; gap: 14px; letter-spacing: 0.3px;
  }
  .footer-web {
    position: absolute; right: 26px; top: 8px; font-size: 21px; letter-spacing: 1px;
  }
</style>
</head>
<body>
<div class="flyer">
  <svg class="flyer-shapes" viewBox="0 0 816 1153" width="816" height="1153">
    <defs>
      <linearGradient id="photoTone" x1="0" y1="0" x2="1" y2="1">
        <stop offset="0" stop-color="#dfe4e8"/>
        <stop offset="0.6" stop-color="#b7c4cf"/>
        <stop offset="1" stop-color="#7f93a5"/>
      </linearGradient>
      <linearGradient id="tealTone" x1="0" y1="0" x2="1" y2="1">
        <stop offset="0" stop-color="#33b8a4"/>
        <stop offset="1" stop-color="#4cc7b5"/>
      </linearGradient>
    </defs>
    <rect role="img" aria-label="Photo of three smiling cleaning staff in uniforms and yellow gloves in a bright office with diamond-shaped windows and cleaning supplies" x="0" y="0" width="816" height="520" fill="url(#photoTone)"/>
    <path d="M0 385 C160 430 380 505 560 498 L816 470 L816 520 L0 520 Z" fill="var(--purple)"/>
    <path d="M0 405 C170 455 390 520 560 510 L816 482 L816 1153 L0 1153 Z" fill="url(#tealTone)"/>
    <path d="M330 520 L620 880 L816 700 L816 482 L560 510 Z" fill="#ffffff" opacity="0.06"/>
    <path d="M0 790 C260 735 560 770 816 945 L816 1153 L0 1153 Z" fill="var(--purple)"/>
    <path d="M0 805 C260 752 560 790 816 960 L816 1153 L0 1153 Z" fill="var(--white)"/>
  </svg>

  <div class="brand">Claremont</div>

  <div class="inset-photo" role="img" aria-label="Photo of a cleaner wiping a desk in an office"></div>

  <h1 class="headline">CLEANING COMPANY</h1>
  <p class="intro">We mainly specialises in <mark>commercial cleaning</mark> such as</p>

  <div class="sectors">
    <div class="sector" style="left:132px">
      <svg width="94" height="94" viewBox="0 0 94 94"><circle cx="47" cy="47" r="45" fill="none" stroke="#fff" stroke-width="2.5"/><g fill="#fff"><rect x="30" y="26" width="34" height="44" rx="2"/><rect x="18" y="42" width="14" height="28"/><rect x="62" y="42" width="14" height="28"/></g><g fill="var(--teal)"><rect x="36" y="32" width="6" height="6"/><rect x="46" y="32" width="6" height="6"/><rect x="56" y="32" width="4" height="6"/><rect x="36" y="44" width="6" height="6"/><rect x="46" y="44" width="6" height="6"/><rect x="56" y="44" width="4" height="6"/><rect x="42" y="58" width="10" height="12"/><rect x="22" y="48" width="6" height="6"/><rect x="66" y="48" width="6" height="6"/></g></svg>
      <span class="sector-name">Office and Building</span>
    </div>
    <div class="sector-divider" style="left:230px"></div>
    <div class="sector" style="left:311px">
      <svg width="94" height="94" viewBox="0 0 94 94"><circle cx="47" cy="47" r="45" fill="none" stroke="#fff" stroke-width="2.5"/><rect x="24" y="20" width="46" height="10" fill="#fff"/><rect x="22" y="32" width="50" height="40" fill="none" stroke="#fff" stroke-width="3"/><path d="M40 72 V56 a7 7 0 0 1 14 0 V72" fill="none" stroke="#fff" stroke-width="3"/><rect x="28" y="40" width="8" height="8" fill="none" stroke="#fff" stroke-width="2.5"/><rect x="58" y="40" width="8" height="8" fill="none" stroke="#fff" stroke-width="2.5"/></svg>
      <span class="sector-name">Educational</span>
    </div>
    <div class="sector-divider" style="left:400px"></div>
    <div class="sector" style="left:489px">
      <svg width="94" height="94" viewBox="0 0 94 94"><circle cx="47" cy="47" r="45" fill="none" stroke="#fff" stroke-width="2.5"/><path d="M22 24 H72 V36 H22 Z" fill="#fff"/><path d="M22 36 q4 6 8 0 q4 6 8 0 q4 6 8 0 q4 6 8 0 q4 6 8 0 q4 6 8 0" fill="none" stroke="#fff" stroke-width="3"/><rect x="24" y="44" width="46" height="28" fill="none" stroke="#fff" stroke-width="3"/><rect x="30" y="50" width="10" height="22" fill="#fff"/><rect x="46" y="50" width="18" height="14" fill="none" stroke="#fff" stroke-width="2.5"/></svg>
      <span class="sector-name">Restaurant</span>
    </div>
    <div class="sector-divider" style="left:579px"></div>
    <div class="sector" style="left:673px">
      <svg width="94" height="94" viewBox="0 0 94 94"><circle cx="47" cy="47" r="45" fill="none" stroke="#fff" stroke-width="2.5"/><g fill="#fff"><path d="M47 20 L74 34 H20 Z"/><rect x="22" y="36" width="50" height="4"/><rect x="26" y="42" width="6" height="22"/><rect x="38" y="42" width="6" height="22"/><rect x="50" y="42" width="6" height="22"/><rect x="62" y="42" width="6" height="22"/><rect x="20" y="66" width="54" height="6"/></g></svg>
      <span class="sector-name">Bank</span>
    </div>
  </div>

  <h2 class="benefits-tab">BENEFITS OF CLEANING</h2>

  <ul class="benefits-col" style="left:37px">
    <li><svg width="13" height="13" viewBox="0 0 13 13"><rect x="0.75" y="0.75" width="11.5" height="11.5" fill="none" stroke="#33a6d7" stroke-width="1.5"/><path d="M3 6.5 L5.5 9 L11 2.5" fill="none" stroke="#33a6d7" stroke-width="1.8"/></svg>Lorem Ipsum is simply dummy text</li>
    <li><svg width="13" height="13" viewBox="0 0 13 13"><rect x="0.75" y="0.75" width="11.5" height="11.5" fill="none" stroke="#33a6d7" stroke-width="1.5"/><path d="M3 6.5 L5.5 9 L11 2.5" fill="none" stroke="#33a6d7" stroke-width="1.8"/></svg>of the printing and typesetting</li>
    <li><svg width="13" height="13" viewBox="0 0 13 13"><rect x="0.75" y="0.75" width="11.5" height="11.5" fill="none" stroke="#33a6d7" stroke-width="1.5"/><path d="M3 6.5 L5.5 9 L11 2.5" fill="none" stroke="#33a6d7" stroke-width="1.8"/></svg>Lorem Ipsum has been the</li>
    <li><svg width="13" height="13" viewBox="0 0 13 13"><rect x="0.75" y="0.75" width="11.5" height="11.5" fill="none" stroke="#33a6d7" stroke-width="1.5"/><path d="M3 6.5 L5.5 9 L11 2.5" fill="none" stroke="#33a6d7" stroke-width="1.8"/></svg>industry's standard dummy text ever</li>
  </ul>
  <ul class="benefits-col" style="left:290px">
    <li><svg width="13" height="13" viewBox="0 0 13 13"><rect x="0.75" y="0.75" width="11.5" height="11.5" fill="none" stroke="#33a6d7" stroke-width="1.5"/><path d="M3 6.5 L5.5 9 L11 2.5" fill="none" stroke="#33a6d7" stroke-width="1.8"/></svg>It is a long established fact that a reader</li>
    <li><svg width="13" height="13" viewBox="0 0 13 13"><rect x="0.75" y="0.75" width="11.5" height="11.5" fill="none" stroke="#33a6d7" stroke-width="1.5"/><path d="M3 6.5 L5.5 9 L11 2.5" fill="none" stroke="#33a6d7" stroke-width="1.8"/></svg>Lorem Ipsum is that it has a</li>
    <li><svg width="13" height="13" viewBox="0 0 13 13"><rect x="0.75" y="0.75" width="11.5" height="11.5" fill="none" stroke="#33a6d7" stroke-width="1.5"/><path d="M3 6.5 L5.5 9 L11 2.5" fill="none" stroke="#33a6d7" stroke-width="1.8"/></svg>Content here, content here'</li>
    <li><svg width="13" height="13" viewBox="0 0 13 13"><rect x="0.75" y="0.75" width="11.5" height="11.5" fill="none" stroke="#33a6d7" stroke-width="1.5"/><path d="M3 6.5 L5.5 9 L11 2.5" fill="none" stroke="#33a6d7" stroke-width="1.8"/></svg>when looking at its layout</li>
  </ul>
  <ul class="benefits-col" style="left:576px">
    <li class="tall"><svg width="13" height="13" viewBox="0 0 13 13"><rect x="0.75" y="0.75" width="11.5" height="11.5" fill="none" stroke="#33a6d7" stroke-width="1.5"/><path d="M3 6.5 L5.5 9 L11 2.5" fill="none" stroke="#33a6d7" stroke-width="1.8"/></svg>It is a long established fact that<br>a reader will be distracted by the</li>
    <li><svg width="13" height="13" viewBox="0 0 13 13"><rect x="0.75" y="0.75" width="11.5" height="11.5" fill="none" stroke="#33a6d7" stroke-width="1.5"/><path d="M3 6.5 L5.5 9 L11 2.5" fill="none" stroke="#33a6d7" stroke-width="1.8"/></svg>readable content of a page</li>
    <li><svg width="13" height="13" viewBox="0 0 13 13"><rect x="0.75" y="0.75" width="11.5" height="11.5" fill="none" stroke="#33a6d7" stroke-width="1.5"/><path d="M3 6.5 L5.5 9 L11 2.5" fill="none" stroke="#33a6d7" stroke-width="1.8"/></svg>established fact that a reader</li>
  </ul>

  <div class="call-now"><span>CALL NOW</span><span class="sep"></span><span>123-456-789</span></div>

  <div class="footer">
    <div class="footer-address">
      <svg width="12" height="16" viewBox="0 0 12 16"><path d="M6 0 a6 6 0 0 1 6 6 c0 4 -6 10 -6 10 s-6 -6 -6 -10 a6 6 0 0 1 6 -6 z" fill="var(--purple)"/><circle cx="6" cy="6" r="2.2" fill="var(--teal)"/></svg>
      <span>comes from a line in section 1.10.32.</span>
    </div>
    <div class="footer-web">www.wesite.com</div>
  </div>
</div>
</body>
</html>
```